Webshop Template

For our Webstore in UK we need a complete Template,
shoppingcart is Magento, the Shop is focussed on Download software,

the name: Appvaultdepot.co.uk

Check out some other good stores, like lumawerk.de

for example the Page from 

www.brenvik.co.uk or

www.lumawerk.de

www.tastenhugo.de

www.klickrabatt.de

The Logodesign which are in Consideration

http://www.artmosaiq.com/design/5520817/logo-design-by-tomasz7kv

http://www.artmosaiq.com/design/5518360/logo-design-by-luisgaviota

http://www.artmosaiq.com/design/5517245/logo-design-by-kestrel-works

http://www.artmosaiq.com/design/5516093/logo-design-by-zumbiloft

http://www.artmosaiq.com/design/5515471/logo-design-by-tivaro

http://www.artmosaiq.com/design/5514902/logo-design-by-blue-fern-graphics-

Target Market(s)

B2C - Consumer Marcet

Industry/Entity Type

Shop

```html
<!DOCTYPE html>
<html lang="en">
<head>
<meta charset="utf-8">
<title>Appvaultdepot – Webshop</title>
<link href="https://fonts.googleapis.com/css2?family=Open+Sans:wght@400;600;700&family=Arimo:wght@400;700&display=swap" rel="stylesheet">
<style>
:root{
  --blue:#0a7fc8;
  --ink:#222;
  --text:#444;
  --line:#ddd;
  --panel:#f6f6f6;
  --footer:#ececec;
  --footer-band:#dcdcdc;
  --orange:#f7941d;
  --orange-dark:#e0640f;
  --logo-grey:#b9b9b9;
}
*{box-sizing:border-box;margin:0;padding:0}
html,body{width:1040px;height:1200px;overflow:hidden;background:#fff}
body{position:relative;font-family:"Arimo",Arial,sans-serif;color:var(--text);font-size:10px}
.abs{position:absolute}
a{color:inherit;text-decoration:none}

/* header */
.brand{left:140px;top:14px;display:flex;align-items:center;gap:8px;font-family:"Open Sans",sans-serif;font-size:24px;font-weight:600;color:#333;letter-spacing:-.5px}
.brand .dot{width:34px;height:34px;border-radius:50%;background:var(--blue)}
.top-links{right:147px;top:9px;font-size:10px;color:#333}
.top-links span{margin:0 7px;color:#999}
.call{left:475px;top:42px;font-size:10px;color:#333}
.call em{font-style:normal;color:var(--blue)}
.search{left:718px;top:40px;width:176px;height:30px;border-radius:15px;background:linear-gradient(#e4e4e4,#fafafa);border:1px solid #ccc}
.search svg{position:absolute;right:12px;top:7px}

.nav{left:139px;top:91px;width:756px;height:42px;background:var(--blue);border-radius:5px;display:flex;font-family:"Open Sans",sans-serif;font-weight:600;font-size:11.5px;color:#fff}
.nav a{display:flex;align-items:center;padding:0 23px;border-right:1px solid rgba(255,255,255,.35)}
.nav a:last-child{border-right:none}

/* hero */
.hero{left:139px;top:159px;width:756px;height:330px;background:var(--panel);border:1px solid var(--line)}
.hero h1{position:absolute;left:22px;top:32px;font-family:"Open Sans",sans-serif;font-weight:400;font-size:37px;line-height:35px;color:var(--ink);letter-spacing:1px}
.hero h1 em{font-style:normal;color:var(--blue)}
.hero p{position:absolute;left:21px;top:149px;width:300px;font-family:"Open Sans",sans-serif;font-size:13.5px;line-height:17.5px;color:#333}
.buy{left:21px;top:242px;width:180px;height:52px;border-radius:26px;background:linear-gradient(var(--orange),var(--orange-dark));color:#fff;font-family:"Open Sans",sans-serif;font-weight:700;font-size:24px;letter-spacing:1px;padding:12px 0 0 24px}
.cart-disc{border-radius:50%;background:linear-gradient(#f58a1f,#b8480c);display:flex;align-items:center;justify-content:center}
.buy-cart{left:178px;top:234px;width:64px;height:64px}
.hero-media{left:340px;top:28px;width:392px;height:292px;border-radius:8px;background:linear-gradient(#2a2a2a 0,#3a3a3a 75%,#cfd2d4 76%,#e8e9ea 100%)}

/* products */
.latest{left:139px;top:518px;width:756px;height:345px;background:var(--panel);border:1px solid var(--line)}
.latest h2{height:38px;background:linear-gradient(#fff,#e6e6e6);font-family:"Open Sans",sans-serif;font-weight:600;font-size:18px;color:var(--blue);padding:8px 0 0 14px;letter-spacing:.5px}
.arrow{top:152px}
.card{top:57px;width:193px;height:266px;background:#fff;border:1px solid var(--line)}
.card h3{text-align:center;margin-top:14px;font-family:"Open Sans",sans-serif;font-weight:400;font-size:14px;color:#333;letter-spacing:.5px}
.card .shot{margin:16px auto 0;width:130px;height:128px;background:linear-gradient(135deg,#d9dde2,#9aa3ad)}
.card p{margin:14px 0 0 26px;width:150px;font-size:10.5px;line-height:13px;color:#444}
.price{position:absolute;left:31px;bottom:11px;width:110px;height:30px;border-radius:15px;background:linear-gradient(var(--orange),var(--orange-dark));color:#fff;font-family:"Open Sans",sans-serif;font-weight:700;font-size:16px;padding:4px 0 0 18px;letter-spacing:.5px}
.price-cart{position:absolute;left:121px;bottom:8px;width:36px;height:36px}

/* partners */
.partners{left:148px;top:886px;width:748px;display:flex;justify-content:space-between;font-family:"Open Sans",sans-serif;font-weight:700;font-size:19px;color:var(--logo-grey);white-space:nowrap}

/* footer */
.footer{left:6px;top:944px;width:1034px;height:256px;background:var(--footer)}
.footer-band{left:6px;top:944px;width:1034px;height:32px;background:var(--footer-band)}
.flinks{top:956px;font-size:10px;color:#333}
.flinks span{margin:0 5px;color:#888}
.social{left:138px;top:988px;display:flex;gap:16px}
.social i{width:31px;height:31px;display:block}
.brand-foot{left:674px;top:985px;display:flex;align-items:center;gap:7px;font-family:"Open Sans",sans-serif;font-size:20px;font-weight:600;color:#333;letter-spacing:-.5px}
.brand-foot .dot{width:30px;height:30px;border-radius:50%;background:var(--blue)}
.fbox{background:#e2e2e2;border-radius:3px}
.col h4{font-family:"Open Sans",sans-serif;font-weight:600;font-size:13px;color:#444;margin-bottom:10px}
.col li{list-style:none;font-size:10px;line-height:13px;color:#555;padding-left:4px}
.pay{display:grid;grid-template-columns:repeat(3,36px);gap:6px 4px;margin-top:4px}
.pay i{display:block;height:24px;border-radius:2px;border:1px solid #bbb}
.contact p{font-size:10px;line-height:11px;color:#444}
.copy{left:137px;top:1171px;font-size:10px;color:#333}
</style>
</head>
<body>

<header>
  <div class="abs brand"><span class="dot"></span>appvaultdepot</div>
  <nav class="abs top-links"><a href="#">Create New Account</a><span>|</span><a href="#">Log In</a><span>|</span><a href="#">Contact Us</a><span>|</span><a href="#">View Cart (0)</a></nav>
  <div class="abs call">Buy <em>Online or Call</em>: 0004 987 6543</div>
  <div class="abs search">
    <svg width="16" height="16" viewBox="0 0 16 16"><circle cx="6" cy="6" r="4.5" fill="none" stroke="#444" stroke-width="1.6"/><line x1="9.5" y1="9.5" x2="14.5" y2="14.5" stroke="#444" stroke-width="2.2"/></svg>
  </div>
  <nav class="abs nav">
    <a href="#">Software</a><a href="#">Computer &amp; Hardware</a><a href="#">Printer</a><a href="#">Displays</a><a href="#">Notebooks</a><a href="#">Telecommunications</a>
  </nav>
</header>

<section class="abs hero">
  <h1>Established fact<br>that a <em>reader will</em><br><em>be</em> distracted.</h1>
  <p>Lorem Ipsum has been the industry's standard dummy text ever since the 1500s, when an unknown printer took a galley of type and scrambled.</p>
  <a class="abs buy" href="#">BUY NOW</a>
  <div class="abs cart-disc buy-cart">
    <svg width="40" height="34" viewBox="0 0 40 34"><path d="M2 4h7l5 18h20l4-13H12" fill="none" stroke="#fff" stroke-width="3.5" stroke-linejoin="round"/><circle cx="16" cy="29" r="3" fill="#fff"/><circle cx="31" cy="29" r="3" fill="#fff"/></svg>
  </div>
  <div class="abs hero-media" role="img" aria-label="Desktop monitor and smartphone showing an online kitchenware shop"></div>
</section>

<section class="abs latest">
  <h2>Lastest Products</h2>
  <svg class="abs arrow" style="left:16px" width="22" height="50" viewBox="0 0 22 50"><path d="M18 2 6 25l12 23" fill="none" stroke="#999" stroke-width="6"/></svg>
  <svg class="abs arrow" style="left:718px" width="22" height="50" viewBox="0 0 22 50"><path d="M4 2l12 23L4 48" fill="none" stroke="#999" stroke-width="6"/></svg>

  <article class="abs card" style="left:52px">
    <h3>App Vault Depot</h3>
    <div class="shot" role="img" aria-label="Dark software product box"></div>
    <p>Valuable branded picnic sets attention with a custom...</p>
    <div class="price">$ 29.90</div>
    <div class="cart-disc price-cart"><svg width="24" height="20" viewBox="0 0 40 34"><path d="M2 4h7l5 18h20l4-13H12" fill="none" stroke="#fff" stroke-width="4"/><circle cx="16" cy="29" r="3.5" fill="#fff"/><circle cx="31" cy="29" r="3.5" fill="#fff"/></svg></div>
  </article>

  <article class="abs card" style="left:281px">
    <h3>App Vault Depot</h3>
    <div class="shot" role="img" aria-label="Orange software pack box with shield" style="background:linear-gradient(135deg,#f39a2a,#c9400e)"></div>
    <p>Valuable branded picnic sets attention with a custom...</p>
    <div class="price">$ 29.90</div>
    <div class="cart-disc price-cart"><svg width="24" height="20" viewBox="0 0 40 34"><path d="M2 4h7l5 18h20l4-13H12" fill="none" stroke="#fff" stroke-width="4"/><circle cx="16" cy="29" r="3.5" fill="#fff"/><circle cx="31" cy="29" r="3.5" fill="#fff"/></svg></div>
  </article>

  <article class="abs card" style="left:505px">
    <h3>App Vault Depot</h3>
    <div class="shot" role="img" aria-label="Blue internet security software box" style="background:linear-gradient(135deg,#2f6fb8,#e9eef4)"></div>
    <p>Valuable branded picnic sets attention with a custom...</p>
    <div class="price">$ 29.90</div>
    <div class="cart-disc price-cart"><svg width="24" height="20" viewBox="0 0 40 34"><path d="M2 4h7l5 18h20l4-13H12" fill="none" stroke="#fff" stroke-width="4"/><circle cx="16" cy="29" r="3.5" fill="#fff"/><circle cx="31" cy="29" r="3.5" fill="#fff"/></svg></div>
  </article>
</section>

<div class="abs partners">
  <span>Zelvapay</span><span>Kordix</span><span>Skeyrun</span><span>Payvoro</span><span>Certavin</span><span>Friendlume</span><span>Nexlinka</span><span>Brisqo</span>
</div>

<footer>
  <div class="abs footer"></div>
  <div class="abs footer-band"></div>
  <nav class="abs flinks" style="left:137px"><a href="#">Site Map</a><span>|</span><a href="#">Search Terms</a><span>|</span><a href="#">Advanced Search</a><span>|</span><a href="#">Orders and Returns</a><span>|</span><a href="#">Contact Us</a></nav>
  <nav class="abs flinks" style="left:705px"><a href="#">Custom Link</a><span>|</span><a href="#">About Us</a><span>|</span><a href="#">Customer Service</a></nav>

  <div class="abs social">
    <i style="background:#3b5998"></i><i style="background:#29a9e0"></i><i style="background:#d9483b"></i><i style="background:#c4302b"></i>
  </div>
  <div class="abs brand-foot"><span class="dot"></span>appvaultdepot</div>

  <div class="abs fbox" style="left:136px;top:1032px;width:592px;height:117px"></div>
  <div class="abs col" style="left:160px;top:1042px"><h4>Customer Service</h4><ul><li>Delivery</li><li>Shipping Methods</li><li>Payment</li><li>Returns &amp; Refund</li><li>Customers</li></ul></div>
  <div class="abs col" style="left:332px;top:1043px"><h4>What's in Store</h4><ul style="margin-top:2px"><li>Women</li><li>Men</li><li>Products A-Z</li><li>Our Brands</li><li>Buy a Gift Card</li></ul></div>
  <div class="abs col" style="left:476px;top:1045px"><h4>Other Sites</h4><ul><li>Second Site</li><li>Friendlume Funpage</li><li>Brisqo</li><li>Skeyrun Plus</li><li>Clipvane</li></ul></div>
  <div class="abs col" style="left:600px;top:1044px"><h4>Easy payment</h4>
    <div class="pay"><i style="background:#fff"></i><i style="background:#c8102e"></i><i style="background:#fff"></i><i style="background:#2c6fb6"></i><i style="background:#eee"></i><i style="background:#ffcc00"></i></div>
  </div>

  <div class="abs fbox" style="left:737px;top:1032px;width:165px;height:117px"></div>
  <div class="abs col contact" style="left:757px;top:1045px"><h4>Contact us</h4>
    <p style="font-size:11px;margin-bottom:6px">+001 (000) 555 742</p>
    <p>Company Inc.</p><p>14 Larkmoor Lane</p><p>Easton, NY 041, USA</p>
  </div>

  <div class="abs copy">Copyright © 2012 appvaultdepot.com. All Rights Reserved.</div>
</footer>

</body>
</html>
```